Australian Civil Construction, Quarry & Mining Services needs a business card

We need a business card designed for our Civil Construction, Quarry & Mining Services based in the country in Australia.
Our Company Brindle Earthworks provide innovate solutions for infrastructure, agricultural and mining (aggregate, sand, roadbase) industry.
We would like our business cards to be double sided
Front of card: black background or something that resembles our business colours. (it doesn't have to be black we are open to options)
- Company name - Brindle Earthworks
- Either our logo or some sort of icon/picture that resembles our business
- Website - https://brindleearthworks-example.com.au/
- We will have a number of different names, positions descriptions, phone numbers and emails on separate cards for each of our managers/directors

```html
<!DOCTYPE html>
<html lang="en">
<head>
<meta charset="utf-8">
<title>Brindle Earthworks – Business Card</title>
<link href="https://fonts.googleapis.com/css2?family=Montserrat:wght@400;700&display=swap" rel="stylesheet">
<style>
  :root {
    --stage: #e4e5e7;
    --card-black: #0a0c0b;
    --pattern-dark: #0f0f0f;
    --pattern-light: #1a1a1a;
    --orange: #f58220;
    --white: #ffffff;
    --divider: #bfbfbf;
  }
  * { margin: 0; padding: 0; box-sizing: border-box; }
  html, body {
    width: 1200px; height: 1200px; overflow: hidden;
    background: var(--stage);
    font-family: "Montserrat", Arial, sans-serif;
  }
  .canvas { position: relative; width: 1200px; height: 1200px; }

  .card {
    position: absolute; top: 453px; width: 515px; height: 294px;
    background: var(--card-black); overflow: hidden;
  }
  .card--front { left: 58px; }
  .card--back { left: 633px; }

  /* front */
  .brand-mark {
    position: absolute; left: 28px; top: 110px; width: 210px;
    text-align: center; color: var(--orange);
    font-weight: 700; font-size: 25px; line-height: 1.2; letter-spacing: 1px;
  }
  .divider {
    position: absolute; left: 257px; top: 56px; width: 1px; height: 184px;
    background: var(--divider);
  }
  .details { position: absolute; left: 274px; top: 53px; width: 232px; color: var(--white); }
  .person-name { font-weight: 700; font-size: 23px; line-height: 1; letter-spacing: .3px; }
  .person-role { color: var(--orange); font-size: 14px; margin-top: 5px; }

  .contact-list { list-style: none; margin-top: 22px; }
  .contact-list li {
    position: relative; padding-left: 20px;
    font-size: 12.5px; line-height: 17px; white-space: nowrap;
  }
  .contact-list li.phone { font-size: 17px; line-height: 20px; margin-bottom: 1px; }
  .contact-list li.web { font-size: 11px; }
  .contact-list li.address { margin-top: 19px; }
  .contact-list svg {
    position: absolute; left: 0; top: 3px; width: 13px; height: 13px;
    fill: none; stroke: var(--orange); stroke-width: 1.6;
  }

  /* back */
  .back-pattern {
    position: absolute; inset: 0;
    background: linear-gradient(135deg, var(--pattern-light), var(--pattern-dark) 50%, var(--pattern-light));
  }
  .back-name {
    position: absolute; left: 0; right: 0; top: 245px;
    text-align: center; color: var(--white);
    font-weight: 700; font-size: 17px; line-height: 24px; letter-spacing: .3px;
  }
</style>
</head>
<body>
<main class="canvas">

  <section class="card card--front">
    <div class="brand-mark">BRINDLE<br>EARTHWORKS</div>
    <div class="divider"></div>
    <div class="details">
      <h1 class="person-name">ALEX MORGAN</h1>
      <p class="person-role">Project Manager</p>
      <ul class="contact-list">
        <li class="phone">
          <svg viewBox="0 0 16 16"><path d="M3 1.5l2.5 0 1.2 3-1.6 1.2c.9 1.9 2.3 3.3 4.2 4.2l1.2-1.6 3 1.2v2.5c0 .8-.7 1.5-1.5 1.5C6.5 13.5 2.5 9.5 1.5 3c0-.8.7-1.5 1.5-1.5z"/></svg>
          03 5550 0192
        </li>
        <li class="email">
          <svg viewBox="0 0 16 16"><rect x="1.5" y="3.5" width="13" height="9"/><path d="M1.5 3.5L8 9l6.5-5.5"/></svg>
          office@brindle-example.com.au
        </li>
        <li class="web">
          <svg viewBox="0 0 16 16"><circle cx="8" cy="8" r="6.5"/><path d="M1.5 8h13M8 1.5c-3 3.5-3 9.5 0 13M8 1.5c3 3.5 3 9.5 0 13"/></svg>
          brindleearthworks-example.com.au
        </li>
        <li class="address">
          <svg viewBox="0 0 16 16"><path d="M8 15s5-5 5-9A5 5 0 0 0 3 6c0 4 5 9 5 9z"/><circle cx="8" cy="6" r="1.8"/></svg>
          27 Carters Lane<br>Tallowvale Victoria 3799<br>Australia
        </li>
      </ul>
    </div>
  </section>

  <section class="card card--back">
    <div class="back-pattern" role="img" aria-label="Dark repeating triangle pattern background"></div>
    <p class="back-name">BRINDLE EARTHWORKS</p>
  </section>

</main>
</body>
</html>
```